Business Cards

Business cards (double-sided) to be handed out to clients and potential clients, with contact details, logo .

Target Market(s)

Small to medium size businesses

Industry/Entity Type

Accountants

Contact Information for Business Card

Brightwater Ledger & Counsel Ltd

Colors

Designer to choose only greyscale colors for use in the design.

Requirements
Must have
• Name, Title, Address, Phone number, Email, Website
Nice to have
• Modern, clean lines, classy
Should not have
• Business cards to be double-sided. Form keeps reverting to single-sided.

```html
<!DOCTYPE html>
<html lang="en">
<head>
<meta charset="utf-8">
<title>Brightwater Ledger &amp; Counsel Ltd — Business Card</title>
<link rel="stylesheet" href="https://fonts.googleapis.com/css2?family=Jost:wght@400&family=Open+Sans:wght@400;600;700&display=swap">
<style>
  :root {
    --page-bg: #a99d9f;
    --front-center: #cbd7d4;
    --front-edge: #8f9d9a;
    --ink: #141414;
    --ink-soft: #2b3034;
    --ink-title: #1f2a36;
    --card-white: #ffffff;
    --band-light: #e8e8e8;
    --band-mid: #d2d2d2;
    --band-grey: #b3b3b3;
    --band-dark: #8e8e8e;
    --rule: #3a3a3a;
  }
  * { margin: 0; padding: 0; box-sizing: border-box; }
  html, body { width: 1200px; height: 960px; overflow: hidden; }
  body {
    background: var(--page-bg);
    font-family: "Open Sans", sans-serif;
    position: relative;
  }
  .card {
    position: absolute;
    left: 255px;
    width: 675px;
    height: 386px;
    overflow: hidden;
  }
  .card--front {
    top: 48px;
    background: radial-gradient(ellipse at 50% 45%, var(--front-center) 0%, var(--front-center) 45%, var(--front-edge) 100%);
    display: flex;
    align-items: center;
    justify-content: center;
  }
  .brand-name {
    font-family: "Jost", sans-serif;
    font-weight: 400;
    color: var(--ink);
    text-align: center;
    letter-spacing: 0.08em;
    text-transform: uppercase;
  }
  .card--front .brand-name { font-size: 34px; line-height: 1.35; width: 420px; margin-top: -40px; }
  .card--back { top: 507px; background: var(--card-white); }
  .card__bands { position: absolute; inset: 0; }
  .card--back .brand-name {
    position: absolute;
    left: 40px; top: 130px;
    width: 220px;
    font-size: 19px;
    line-height: 1.3;
    text-align: left;
  }
  .divider {
    position: absolute;
    left: 308px; top: 89px;
    width: 3px; height: 128px;
    background: linear-gradient(var(--card-white), var(--rule) 20%, var(--rule) 80%, var(--card-white));
  }
  .person { position: absolute; left: 335px; top: 34px; }
  .person__name { font-size: 24px; font-weight: 700; color: var(--ink-soft); letter-spacing: 0.02em; }
  .person__title { font-size: 16px; color: var(--ink-title); margin-top: 2px; }
  .contact { position: absolute; left: 328px; list-style: none; }
  .contact__item { display: flex; align-items: flex-start; gap: 14px; font-size: 16px; color: #111; line-height: 22px; position: absolute; left: 0; white-space: nowrap; }
  .contact__icon { width: 29px; height: 29px; flex: none; margin-top: -4px; }
  .website {
    position: absolute; left: 0; width: 690px; top: 330px;
    text-align: center; font-size: 16px; color: #111;
  }
</style>
</head>
<body>
  <section class="card card--front" aria-label="Card front">
    <p class="brand-name">Brightwater Ledger &amp; Counsel Ltd</p>
  </section>

  <section class="card card--back" aria-label="Card back">
    <svg class="card__bands" viewBox="0 0 675 385" width="675" height="385" aria-hidden="true">
      <polygon points="0,266 297,266 377,385 0,385" fill="var(--band-light)"/>
      <polygon points="0,311 333,311 382,385 0,385" fill="var(--band-mid)"/>
      <polygon points="333,311 537,311 585,385 382,385" fill="var(--band-grey)"/>
      <polygon points="385,362 675,362 675,385 400,385" fill="var(--band-dark)"/>
    </svg>

    <p class="brand-name">Brightwater Ledger &amp; Counsel Ltd</p>
    <div class="divider"></div>

    <div class="person">
      <h1 class="person__name">DANIEL MARSH</h1>
      <p class="person__title">Chief Financial Consultant</p>
    </div>

    <ul class="contact">
      <li class="contact__item" style="top:158px">
        <svg class="contact__icon" viewBox="0 0 30 30"><circle cx="15" cy="15" r="13.5" fill="none" stroke="#222" stroke-width="1.2"/><path d="M11 9.5c-.6.4-1.3 1.2-1.1 2.6.4 3 4 7.2 7.2 8.3 1.4.4 2.3-.1 2.8-.7l.5-.6-2.6-2-1.2 1c-1.5-.6-3.2-2.5-3.8-4l1-1.2-1.8-2.8z" fill="#222"/></svg>
        <span>742-555-0188</span>
      </li>
      <li class="contact__item" style="top:197px">
        <svg class="contact__icon" viewBox="0 0 30 30"><circle cx="15" cy="15" r="13.5" fill="none" stroke="#222" stroke-width="1.2"/><text x="15" y="20" text-anchor="middle" font-family="Open Sans, sans-serif" font-weight="700" font-size="14" fill="#222">@</text></svg>
        <span>hello@brightwaterledger.com</span>
      </li>
      <li class="contact__item" style="top:236px">
        <svg class="contact__icon" viewBox="0 0 30 30"><circle cx="15" cy="15" r="13.5" fill="none" stroke="#222" stroke-width="1.2"/><path d="M15 8a4.5 4.5 0 0 0-4.5 4.5c0 3.3 4.5 8.5 4.5 8.5s4.5-5.2 4.5-8.5A4.5 4.5 0 0 0 15 8zm0 6.2a1.7 1.7 0 1 1 0-3.4 1.7 1.7 0 0 1 0 3.4z" fill="#222"/></svg>
        <span>48 Harbor Row, Suite 310, Linden<br>NMLS 60417</span>
      </li>
    </ul>

    <p class="website">www.brightwaterledger.com</p>
  </section>
</body>
</html>
```